Wine Label Design

A wine label for 750ml bottles. Same label for different varieties with the variety / region / vintage to be updated as required.
Brand: Beyond the Ridge
Product Use: Front and Back label suitable for a 750 ml bottle (preferably Burgundy bottles)
Design Brief: Beyond the Ridge is a small winery that produces limited amounts of hand crafted wines that are aimed at the mid to top end of the market and requires a label befitting the work that goes into the creation of the wine. In terms of style i don't have any preconceptions and am open to a broad range of design suggestions at the same level of existing premium brands or innovative brands.
Must Have for Front label
Front Label
Beyond the Ridge
2013
Grampians
Shiraz
750ML (should be in smaller text)
Alc. 14% by Vol. (should be in smaller text)
Must Have for Back Label
Beyond the Ridge
2013
Grampians
Shiraz
www.beyondtheridge.com.au (should be in smaller text)
Product of Australia
Alc.14% by Vol. (should be in smaller text)
Contains preservative 220(should be in smaller text)
Below are some guides for dimensions:
The Front Label Size can be between
100 - 120 mm (Width) x 70 - 85 mm (Height)
The back label size can be between
90 mm (Width) x 70 - 85 mm (Height)
Updates
Target Market(s)
Medium to top end of the wine market who require the label to be a reflection of the wine.
Industry/Entity Type
Product
Colors
Designer to choose colors to be used in the design.
Look and feel
Each slider illustrates characteristics of the customer's brand and the style your logo design should communicate.

```html
<!DOCTYPE html>
<html lang="en">
<head>
<meta charset="utf-8">
<title>Beyond the Ridge – 2013 Grampians Shiraz Front Label</title>
<link rel="stylesheet" href="https://fonts.googleapis.com/css2?family=EB+Garamond:wght@400&display=swap">
<style>
  :root {
    --paper: #f2ede5;
    --ink: #47403f;
    --frame: #141212;
    --backdrop: #ffffff;
  }
  html, body {
    margin: 0;
    padding: 0;
    width: 855px;
    height: 1200px;
    overflow: hidden;
    background: var(--backdrop);
  }
  .label {
    position: relative;
    width: 855px;
    height: 1200px;
    box-sizing: border-box;
    background: var(--paper);
    font-family: "EB Garamond", Garamond, "Times New Roman", serif;
    color: var(--ink);
  }
  .label__frame {
    position: absolute;
    inset: 14px;
    border: 4px solid var(--frame);
    pointer-events: none;
  }
  .label__line {
    position: absolute;
    left: 0;
    right: 0;
    margin: 0;
    text-align: center;
    font-weight: 400;
    line-height: 1;
  }
  .brand-name {
    top: 196px;
    font-size: 116px;
    line-height: 1.08;
  }
  .vintage {
    top: 588px;
    font-size: 94px;
  }
  .region {
    top: 763px;
    font-size: 44px;
  }
  .variety {
    top: 873px;
    font-size: 44px;
  }
  .volume {
    top: 1031px;
    font-size: 21px;
  }
  .alcohol {
    top: 1122px;
    font-size: 21px;
  }
</style>
</head>
<body>
  <main class="label">
    <div class="label__frame"></div>
    <h1 class="label__line brand-name">Beyond<br>the Ridge</h1>
    <p class="label__line vintage">2013</p>
    <p class="label__line region">Grampians</p>
    <p class="label__line variety">Shiraz</p>
    <p class="label__line volume">750ML</p>
    <p class="label__line alcohol">Alc. 14% by Vol.</p>
  </main>
</body>
</html>
```